New Business Card Design Project

I need a clean, professional business card. I'd like it to have some color, but not be wild. We do technology consulting and we have clients large and small who trust us with some of their most important data and projects. Simple but not boring should drive all design proposals. Multicolored and two sided, but with a matte finish, I think.
For more on tone, check out our website: http://quorvantis.example

Target Market(s)

Upper management of respected businesses. Tech savvy, but not "hipster".

Industry/Entity Type

Business

Requirements
Must have
• Files need to be provided in .eps and in .pdf in a manner that allows for easy updates.
Must have Name, Title, Phone, Email, Twitter, Website
Nice to have
• Logo/Name shouldn't be too big. One thing I've read several places is that the bigger the logo, the smaller the brand. A good article on dos and don'ts here: http://www.brindlepost.example/2011/02/business-card-experience.html

```html
<!DOCTYPE html>
<html lang="en">
<head>
<meta charset="utf-8">
<title>Quorvantis Business Card</title>
<link rel="stylesheet" href="https://fonts.googleapis.com/css2?family=Open+Sans:wght@400;600&display=swap">
<style>
  :root {
    --canvas-bg: #e4e5e7;
    --card-bg: #ffffff;
    --card-shadow: rgba(0, 0, 0, 0.18);
    --brand-grey: #6d6f72;
    --text-grey: #8a8c8f;
    --accent-teal: #1b9bb0;
    --accent-green: #7cb342;
    --accent-dot: #2a6fa8;
  }
  * { box-sizing: border-box; margin: 0; padding: 0; }
  html, body {
    width: 1200px;
    height: 900px;
    overflow: hidden;
    background: var(--canvas-bg);
    font-family: "Open Sans", Arial, sans-serif;
  }
  .canvas {
    width: 1200px;
    height: 900px;
    display: flex;
    flex-direction: column;
    align-items: center;
    justify-content: center;
    gap: 60px;
  }
  .card {
    position: relative;
    width: 560px;
    height: 320px;
    background: var(--card-bg);
    box-shadow: 0 6px 22px var(--card-shadow);
  }
  .brand {
    position: absolute;
    display: flex;
    align-items: center;
    gap: 12px;
  }
  .brand-dot {
    width: 12px;
    height: 12px;
    border-radius: 50%;
    background: var(--accent-green);
  }
  .brand-name {
    font-weight: 400;
    font-size: 24px;
    letter-spacing: 2px;
    color: var(--brand-grey);
    text-transform: uppercase;
  }
  /* Back side */
  .card-back .brand { left: 48px; top: 138px; }
  .website {
    position: absolute;
    left: 48px;
    bottom: 36px;
    font-size: 12px;
    color: var(--accent-teal);
  }
  /* Front side */
  .card-front .brand { right: 48px; top: 48px; }
  .person {
    position: absolute;
    left: 48px;
    top: 112px;
  }
  .person-name {
    font-size: 22px;
    color: var(--accent-teal);
    line-height: 1.2;
  }
  .person-title {
    font-size: 11px;
    color: var(--text-grey);
    letter-spacing: 0.5px;
    margin-top: 2px;
  }
  .contact-list {
    position: absolute;
    left: 260px;
    bottom: 44px;
    list-style: none;
    font-size: 14px;
    color: var(--text-grey);
    line-height: 1.55;
  }
  .contact-item {
    display: flex;
    align-items: center;
    gap: 8px;
  }
  .contact-icon {
    width: 14px;
    height: 14px;
    flex: none;
    display: flex;
    align-items: center;
    justify-content: center;
  }
  .icon-at { font-size: 13px; color: var(--text-grey); }
  .icon-social {
    width: 9px;
    height: 9px;
    border-radius: 50%;
    background: var(--accent-dot);
  }
</style>
</head>
<body>
<main class="canvas">
  <section class="card card-back" aria-label="Card back">
    <div class="brand">
      <span class="brand-dot"></span>
      <span class="brand-name">Quorvantis</span>
    </div>
    <p class="website">www.quorvantis.example</p>
  </section>

  <section class="card card-front" aria-label="Card front">
    <div class="brand">
      <span class="brand-dot"></span>
      <span class="brand-name">Quorvantis</span>
    </div>
    <div class="person">
      <p class="person-name">Dana Whitlow</p>
      <p class="person-title">CEO</p>
    </div>
    <ul class="contact-list">
      <li class="contact-item">
        <span class="contact-icon">
          <svg width="9" height="13" viewBox="0 0 9 13" aria-hidden="true">
            <rect x="0.75" y="0.75" width="7.5" height="11.5" rx="1.5" fill="none" stroke="var(--accent-green)" stroke-width="1.5"/>
            <rect x="3" y="9.5" width="3" height="1" fill="var(--accent-green)"/>
          </svg>
        </span>
        1-800-555-0142, ext. 700
      </li>
      <li class="contact-item">
        <span class="contact-icon icon-at">@</span>
        dana@quorvantis.example
      </li>
      <li class="contact-item">
        <span class="contact-icon"><span class="icon-social"></span></span>
        @quorvantis
      </li>
    </ul>
  </section>
</main>
</body>
</html>
```